Masonry and Landscaping Construction company business card

Looking for a business card design for a construction company named Ferrano Construction. It is an italian-american family business that specializes in custom stone work, patios, walkways, driveways, steps, outdoor kitchens, concrete, waterproofing, power wash, landscaping and more. Our colors are mostly red and white with some black. We're looking for a bold design. we also like to incorporate a picture of my family's hometown somewhere in it.
Target Market(s)
Luxury home owners
Industry/Entity Type
Construction
Contact Information for Business Card
Details includes should be bullet points mentioning the services provided. Custom Stone Work, Outdoor Kitchens, Fire Pits, Patios, Walkways, Steps, Concrete, Waterproofing, powerwash and landscaping
Requirements
Must have
- Would like a spot on the card for co-owners names, numbers and email to be listed also looking to add the QR code for an instagram page
Nice to have
- would like something bold, based around the colors red and white with black outlines or details

```html
<!DOCTYPE html>
<html lang="en">
<head>
<meta charset="utf-8">
<title>Ferrano Construction – Business Card</title>
<link href="https://fonts.googleapis.com/css2?family=Archivo+Black&family=Poppins:wght@400;500;700&display=swap" rel="stylesheet">
<style>
  :root {
    --red: #e3101e;
    --black: #141414;
    --ink: #2a2a2a;
    --white: #ffffff;
    --paper: #f3f3f3;
    --stage: #2b2b2b;
    --divider: #cfcfcf;
    --town-dark: #2e2f2a;
    --town-mid: #4a4a3d;
    --town-green: #3d4a30;
  }
  * { margin: 0; padding: 0; box-sizing: border-box; }
  html, body { width: 1200px; height: 900px; overflow: hidden; }
  body {
    background: var(--stage);
    font-family: "Poppins", sans-serif;
    position: relative;
  }
  .card {
    position: absolute;
    left: 250px;
    width: 700px;
    height: 400px;
    border-radius: 26px;
    overflow: hidden;
    border-bottom: 7px solid var(--red);
  }
  /* Front */
  .card-front { top: 40px; background: var(--paper); }
  .brand-block {
    position: absolute;
    left: 40px; top: 0; width: 290px; height: 393px;
    display: flex; align-items: center; justify-content: center; gap: 12px;
  }
  .brand-square {
    width: 26px; height: 26px; background: var(--red); flex: none;
  }
  .brand-name {
    font-family: "Poppins", sans-serif;
    font-weight: 700;
    font-size: 25px;
    line-height: 1.1;
    color: var(--black);
    text-transform: uppercase;
  }
  .front-divider {
    position: absolute; left: 352px; top: 70px;
    width: 1px; height: 250px; background: var(--divider);
  }
  .contact-block { position: absolute; left: 385px; top: 95px; }
  .person-name {
    font-family: "Archivo Black", sans-serif;
    font-size: 27px; letter-spacing: 1px;
    color: var(--black); text-transform: uppercase;
  }
  .person-title { color: var(--red); font-size: 19px; margin-top: 2px; }
  .contact-list { list-style: none; margin-top: 28px; }
  .contact-list li {
    display: flex; align-items: center; gap: 12px;
    font-size: 17px; color: var(--ink); margin-bottom: 8px;
  }
  .contact-list svg { width: 18px; height: 18px; flex: none; }

  /* Back */
  .card-back { top: 470px; background: var(--town-dark); }
  .town-photo {
    position: absolute; inset: 0;
    background: linear-gradient(160deg, var(--town-green) 0%, var(--town-mid) 45%, var(--town-dark) 100%);
  }
  .town-shade { position: absolute; inset: 0; background: rgba(0,0,0,0.45); }
  .back-brand {
    position: absolute; top: 38px; left: 0; right: 0;
    display: flex; justify-content: center; align-items: center; gap: 14px;
  }
  .back-brand .brand-name { color: var(--white); font-size: 40px; }
  .back-brand .brand-square { width: 34px; height: 34px; }
  .services {
    position: absolute; top: 170px; left: 90px; right: 60px;
    display: flex; gap: 80px;
  }
  .service-list { list-style: none; }
  .service-list li {
    display: flex; align-items: center; gap: 12px;
    color: var(--white); font-size: 21px; line-height: 1.55;
  }
  .bullet {
    width: 14px; height: 14px; border: 2px solid var(--red);
    border-radius: 3px; position: relative; flex: none;
  }
  .bullet::after {
    content: ""; position: absolute; inset: 2px; background: var(--red);
  }
</style>
</head>
<body>

<section class="card card-front">
  <div class="brand-block">
    <span class="brand-square"></span>
    <span class="brand-name">Ferrano<br>Construction</span>
  </div>
  <div class="front-divider"></div>
  <div class="contact-block">
    <h1 class="person-name">Marco Ferrano</h1>
    <p class="person-title">Managing Director</p>
    <ul class="contact-list">
      <li>
        <svg viewBox="0 0 24 24"><path fill="#e3101e" d="M6.6 10.8a15.1 15.1 0 0 0 6.6 6.6l2.2-2.2a1 1 0 0 1 1-.25 11.4 11.4 0 0 0 3.6.57 1 1 0 0 1 1 1V20a1 1 0 0 1-1 1A17 17 0 0 1 3 4a1 1 0 0 1 1-1h3.5a1 1 0 0 1 1 1c0 1.25.2 2.45.57 3.57a1 1 0 0 1-.25 1z"/></svg>
        044-555 018 274
      </li>
      <li>
        <svg viewBox="0 0 24 24"><path fill="#e3101e" d="M2 5h20v14H2z"/><path fill="none" stroke="#f3f3f3" stroke-width="1.6" d="M2 5l10 8 10-8"/></svg>
        info@ferranobuild.com
      </li>
      <li>
        <svg viewBox="0 0 24 24"><circle cx="12" cy="12" r="10" fill="none" stroke="#e3101e" stroke-width="2"/><ellipse cx="12" cy="12" rx="4.5" ry="10" fill="none" stroke="#e3101e" stroke-width="1.6"/><path d="M2 12h20M4 7h16M4 17h16" stroke="#e3101e" stroke-width="1.4"/></svg>
        www.ferranobuild.com
      </li>
    </ul>
  </div>
</section>

<section class="card card-back">
  <div class="town-photo" role="img" aria-label="Photograph of the family's Italian hometown: stone buildings among green hills"></div>
  <div class="town-shade"></div>
  <div class="back-brand">
    <span class="brand-square"></span>
    <span class="brand-name">Ferrano Construction</span>
  </div>
  <div class="services">
    <ul class="service-list">
      <li><span class="bullet"></span>Custom Stone Work</li>
      <li><span class="bullet"></span>Outdoor Kitchens</li>
      <li><span class="bullet"></span>Fire Pits</li>
      <li><span class="bullet"></span>Patios</li>
      <li><span class="bullet"></span>Walkways</li>
    </ul>
    <ul class="service-list">
      <li><span class="bullet"></span>Steps</li>
      <li><span class="bullet"></span>Concrete</li>
      <li><span class="bullet"></span>Waterproofing</li>
      <li><span class="bullet"></span>Power Wash</li>
      <li><span class="bullet"></span>Landscaping</li>
    </ul>
  </div>
</section>

</body>
</html>
```